Word template for proposals we send to clients

We want a word template designed based on the look/feel of our website. The website is www.brovanex.com.au and while we have pictures of 2 staff on the website we have pictures of other staff if required

the template will be used to send out proposals to potential clients, therefore it has to be professional, modern and compelling for someone to open

Target Market(s)

B2B

Industry/Entity Type

It Company

Font styles to use
Serif

Colors

Designer to choose colors to be used in the design.

Requirements
Must have
• Same look and feel as website
Nice to have
• Dont know what I am missing so anythign you feel i need to add

```html
<!DOCTYPE html>
<html lang="en">
<head>
<meta charset="utf-8">
<title>Brovanex Consulting Services – Brochure</title>
<link href="https://fonts.googleapis.com/css2?family=Open+Sans:wght@400;600;700&display=swap" rel="stylesheet">
<style>
  :root{
    --navy:#313945;
    --lime:#b5c22f;
    --olive:#6b8e3c;
    --ink:#2a2a2a;
    --rule:#b9b9b9;
    --paper:#ffffff;
  }
  *{box-sizing:border-box;margin:0;padding:0}
  html,body{width:1200px;height:1200px;overflow:hidden}
  body{background:linear-gradient(#5a5a5a,#262626);font-family:"Open Sans",sans-serif;color:var(--ink);position:relative}
  .page{position:absolute;top:253px;width:553px;height:781px;background:var(--paper);overflow:hidden}
  .page--front{left:34px}
  .page--back{left:616px}

  /* front */
  .front-header{position:absolute;left:0;top:0;width:100%;height:127px;background:var(--navy);display:flex;flex-direction:column;align-items:center;justify-content:center}
  .brand-name{font-weight:700;font-size:38px;color:var(--lime);line-height:1;letter-spacing:1px}
  .brand-sub{font-weight:700;font-size:15px;color:#fff;letter-spacing:3px;margin-top:6px}
  .intro{position:absolute;left:30px;top:187px;width:492px;height:145px;border:1px solid var(--rule);padding:32px 10px 0;text-align:center;font-size:11.6px;line-height:15.3px}
  .intro-title{position:absolute;top:-21px;left:50%;transform:translateX(-50%);background:var(--paper);padding:0 10px;white-space:nowrap;font-weight:700;font-size:29px;color:var(--lime);line-height:1.3}
  .team-band{position:absolute;left:0;top:443px;width:100%;height:254px;background:var(--lime)}
  .photo{position:absolute;border-radius:40px 40px 0 0}
  .photo--support{left:22px;top:371px;width:264px;height:326px;background:linear-gradient(160deg,#c9a98f,#8b7aa8 60%,#5a4f6a)}
  .photo--systems{left:302px;top:355px;width:224px;height:342px;background:linear-gradient(160deg,#c9a184,#dfe7ee 55%,#c84b24)}
  .name-tag{position:absolute;font-size:8px;font-weight:600;line-height:1.15;text-align:center}
  .name-tag b{display:block;font-size:9.5px;font-weight:700}
  .name-tag--support{left:182px;top:404px}
  .name-tag--systems{left:456px;top:437px}

  .contact-bar{position:absolute;left:0;bottom:0;width:100%;background:var(--olive);color:#fff;font-size:10.8px;line-height:14.5px;display:flex;align-items:center;white-space:nowrap}
  .page--front .contact-bar{height:84px;padding-left:30px}
  .page--back .contact-bar{height:60px;padding-left:30px}
  .contact{display:flex;align-items:center;gap:9px}
  .contact svg{width:10px;height:10px;fill:#fff;flex:none}
  .contact--mail{width:202px}
  .contact--phone{width:144px}
  .page--back .contact--mail{width:204px}
  .page--back .contact--phone{width:143px}

  /* back */
  .about-box{position:absolute;left:11px;top:0;width:205px;height:129px;background:var(--navy);color:#fff;font-weight:700;font-size:21.5px;display:flex;align-items:center;justify-content:center;letter-spacing:.5px}
  .side-band{position:absolute;left:11px;top:139px;width:205px;height:582px;background:var(--lime)}
  .side-item{position:absolute;left:0;width:100%;text-align:center;color:#fff;font-weight:700;font-size:18.5px;letter-spacing:.3px}
  .side-item svg{display:block;margin:0 auto 4px;fill:#fff;stroke:#fff}
  .side-item--philosophy{top:44px}
  .side-item--success{top:222px}
  .side-item--director{top:444px}

  .copy-column{position:absolute;left:235px;top:27px;width:299px;display:flex;flex-direction:column;font-size:8.9px;line-height:12.5px;letter-spacing:-0.15px;text-align:justify}
  .copy p{margin:0}
  .copy .gap{margin-top:12px}
  .copy--philosophy{margin-top:22px}
  .copy--success{margin-top:10px;border-top:1px solid var(--rule);padding-top:9px}
  .copy--director{margin-top:10px;border-top:1px solid var(--rule);padding-top:9px}
</style>
</head>
<body>

<section class="page page--front">
  <header class="front-header">
    <div class="brand-name">Brovanex</div>
    <div class="brand-sub">CONSULTING SERVICES</div>
  </header>

  <div class="intro">
    <h1 class="intro-title">IT SUPPORT + PERSONALITY</h1>
    <p>Melbourne based IT Support that you can count on.<br>
    Every day small and medium businesses rely on Brovanex Consulting Services to keep their technology running smoothly. When you become a valued client of Brovanex you gain an IT partner who is on call 24/7. Whether we're creating a user, resolving performance issues, getting clients up-and-running after natural disasters or remediating ransomware, your IT support team is here for you.</p>
  </div>

  <div class="team-band"></div>
  <div class="photo photo--support" role="img" aria-label="Cut-out photo of a smiling support engineer in a headset holding an open laptop"></div>
  <div class="photo photo--systems" role="img" aria-label="Cut-out photo of a senior systems engineer holding a server handbook"></div>
  <div class="name-tag name-tag--support"><b>MATEO</b>Support Engineer</div>
  <div class="name-tag name-tag--systems"><b>LIAM</b>Senior Systems<br>Engineer</div>

  <footer class="contact-bar">
    <div class="contact contact--mail"><svg viewBox="0 0 10 10"><path d="M0 2h10v6H0z" fill="#fff"/><path d="M0.6 2.4L5 5.4 9.4 2.4" fill="none" stroke="#6b8e3c" stroke-width=".8"/></svg><span>info@brovanex.com.au<br>support@brovanex.com.au</span></div>
    <div class="contact contact--phone"><svg viewBox="0 0 10 10"><path d="M1 4c0-2 8-2 8 0v1H7V4H3v1H1z M2.5 5.5h5L9 9H1z"/></svg><span>1300 555 017<br>+61 3 5550 1274</span></div>
    <div class="contact"><svg viewBox="0 0 10 10"><path d="M5 0a3.5 3.5 0 0 1 3.5 3.5C8.5 6 5 10 5 10S1.5 6 1.5 3.5A3.5 3.5 0 0 1 5 0zm0 2a1.5 1.5 0 1 0 0 3 1.5 1.5 0 0 0 0-3z"/></svg><span>Lvl 9/210 Harlow St<br>Melbourne VIC 3000 Australia</span></div>
  </footer>
</section>

<section class="page page--back">
  <div class="about-box">ABOUT US</div>
  <div class="side-band">
    <div class="side-item side-item--philosophy">
      <svg width="14" height="26" viewBox="0 0 14 26"><path d="M9 0L1 14h5l-3 12 10-16H8z" stroke="none"/></svg>
      OUR PHILOSOPHY
    </div>
    <div class="side-item side-item--success">
      <svg width="34" height="32" viewBox="0 0 34 32"><path d="M8 1h18v9a9 9 0 0 1-18 0z" stroke="none"/><path d="M8 4H2c0 6 3 9 7 9M26 4h6c0 6-3 9-7 9" fill="none" stroke-width="3"/><path d="M14 18h6v6h5v6H9v-6h5z" stroke="none"/></svg>
      OUR SUCCESS
    </div>
    <div class="side-item side-item--director">
      <svg width="34" height="34" viewBox="0 0 34 34"><circle cx="17" cy="17" r="15" fill="none" stroke-width="3"/><circle cx="17" cy="13" r="5" stroke="none"/><path d="M8 26c2-5 16-5 18 0z" stroke="none"/></svg>
      OUR DIRECTOR
    </div>
  </div>

  <div class="copy-column">
    <div class="copy copy--about">
      <p>Everything we do is focused on providing real, measurable benefits to your organisation by improving reliability, performance and collaborating strategically with you to implement enhancements to existing systems and processes.</p>
      <p>As a Nimbus Silver Small and Midmarket Cloud Solutions Partner and Nimbus Small Business Specialist, Brovanex supports and configures IT systems for small to medium businesses using Nimbus technologies.</p>
    </div>

    <div class="copy copy--philosophy">
      <p>Since our beginnings in 2006, the Brovanex philosophy has always been: “We are a Customer Service Company; that just happens to fix IT Systems”. This remains our philosophy today, and is Owner &amp; Director Daniel Okafor's favourite saying about how we serve our customers today.</p>
      <p>Other companies have tried to mirror the Brovanex model (but many have failed):</p>
      <p>• Fixed Monthly Pricing &nbsp; • 5 Minute Response Guarantee<br>• 24/7 &amp; 365 days support</p>
    </div>

    <div class="copy copy--success">
      <p>The secret to Brovanex's success? Our staff!</p>
      <p>At Brovanex, we give our staff the freedom to be themselves. Not only are all staff technically trained, they are the forefront of our customer service.</p>
      <p>We are not happy until the customer is happy!</p>
      <p>We are very proud of the staff we employ at Brovanex and it's our staff that sets us apart from our peers. Our staff come from varying experience but they all have the one thing in common and that is service.</p>
      <p>We are simply not happy until the client is happy.</p>
      <p>When recruiting we look for personalities that match are ethos which is provide the level of service we would expect if we were the client.</p>
      <p>All staff are required to maintain and attain industry qualifications, but qualification is only one part of the equation, experience is necessary as well.</p>
      <p>We ensure that all staff have a minimum of 3 years experience in IT.</p>
    </div>

    <div class="copy copy--director">
      <p>Daniel Okafor setup Brovanex Consulting Services to provide unmatched IT service/support at a True Fixed Monthly Cost. Brovanex has redesigned the landscape of IT support for SME's in Australia by truly providing a new level of service that has not been seen before.</p>
      <p class="gap">We are constantly setting new trends and goals and is further demonstrated by being one of the first IT providers in Australia truly providing a fixed fee model rather than the typical ad-hoc packages.</p>
      <p class="gap">Daniel Okafor has over 14 years experience in the IT industry having worked in Melbourne, London, New York, Chicago, San Francisco and Luxembourg. His corporate IT background is extensive having worked for Vantor Systems, Keller Media, Department Of Justice, Granite Ridge Capital as well as numerous other companies. Daniel understands the critical nature of IT infrastructure and the demand of technical and proactive support to maintain maximum uptime.</p>
    </div>
  </div>

  <footer class="contact-bar">
    <div class="contact contact--mail"><svg viewBox="0 0 10 10"><path d="M0 2h10v6H0z" fill="#fff"/><path d="M0.6 2.4L5 5.4 9.4 2.4" fill="none" stroke="#6b8e3c" stroke-width=".8"/></svg><span>info@brovanex.com.au<br>support@brovanex.com.au</span></div>
    <div class="contact contact--phone"><svg viewBox="0 0 10 10"><path d="M1 4c0-2 8-2 8 0v1H7V4H3v1H1z M2.5 5.5h5L9 9H1z"/></svg><span>1300 555 017<br>+61 3 5550 1274</span></div>
    <div class="contact"><svg viewBox="0 0 10 10"><path d="M5 0a3.5 3.5 0 0 1 3.5 3.5C8.5 6 5 10 5 10S1.5 6 1.5 3.5A3.5 3.5 0 0 1 5 0zm0 2a1.5 1.5 0 1 0 0 3 1.5 1.5 0 0 0 0-3z"/></svg><span>Lvl 9/210 Harlow St<br>Melbourne VIC 3000 Australia</span></div>
  </footer>
</section>

</body>
</html>
```